New Business Card Design for Engineering and Surveying Company

We need a new design template for our business cards. We are a civil engineering, land surveying and pipeline integrity business. Please see dkhpartners.com for details. We need a bold, new business card design to complement our rebranding and marketing program. We have anew logo and attached vectro file. Please find additional details below. I am available to answer any questions.

Target Market(s)

Contractors, business owners, oil companies

Contact Information for Business Card

Needs to be customizable for different people (name, title, cell)

Font styles to use
Sans Serif
Other font styles liked:
• See eps file

Requirements
Must have
• Example Information:
Trevor Ashcombe

T:318-555-0173
M: 646-555-0148
tashcombe@dkhprtnrs.com

Address: 1875 Pinecrest Parkway, Cedar Hollow, Texas 75990
Email: tolvanrey@dkhpartners.com
Website: www.dkhpartners.com
Nice to have
• I would like the back of the card to have the logo on a bold background with the text below:

[logo]
DORAN KESSLING & PARTNERS
CIVIL ENGINEERING | LAND SURVEYING | PIPELINE INTEGRITY

The reverse side should have the contact information for the person (example above), a smaller version of the logo and a graphic

```html
<!DOCTYPE html>
<html lang="en">
<head>
<meta charset="utf-8">
<title>DKH Partners Business Card</title>
<link rel="stylesheet" href="https://fonts.googleapis.com/css2?family=Open+Sans:wght@400;600;800&display=swap">
<style>
  :root {
    --backdrop: #2a2c30;
    --card-white: #ffffff;
    --brand-red: #d42028;
    --brand-blue: #1f55b0;
    --brand-blue-dark: #173f86;
    --ink: #111114;
  }
  * { box-sizing: border-box; margin: 0; padding: 0; }
  html, body { width: 1200px; height: 900px; overflow: hidden; }
  body {
    background: var(--backdrop);
    font-family: "Open Sans", sans-serif;
    position: relative;
  }
  .card {
    position: absolute;
    left: 330px;
    width: 540px;
    height: 310px;
    border-radius: 22px;
    overflow: hidden;
    background: var(--card-white);
    box-shadow: 0 10px 30px rgba(0,0,0,.45);
  }
  .card--front { top: 90px; }
  .card--back { top: 480px; background: var(--brand-red); }

  .wordmark {
    display: flex;
    align-items: center;
    gap: 14px;
    color: var(--ink);
    font-weight: 800;
    letter-spacing: 2px;
  }
  .wordmark__square { background: var(--brand-red); }

  .card--front .wordmark {
    position: absolute;
    left: 0; right: 0; top: 105px;
    justify-content: center;
    font-size: 78px;
    line-height: 1;
  }
  .card--front .wordmark__square { width: 30px; height: 30px; }

  .edge-strip {
    position: absolute;
    left: 0; right: 0; bottom: 0;
    height: 26px;
    display: flex;
  }
  .edge-strip__red { background: var(--brand-red); }
  .edge-strip__red--lead { width: 110px; }
  .edge-strip__red--tail { flex: 1; }
  .edge-strip__blue {
    width: 250px;
    background: var(--brand-blue);
    color: #fff;
    font-size: 13px;
    font-weight: 600;
    display: flex;
    align-items: center;
    justify-content: center;
    letter-spacing: .3px;
  }

  .logo-panel {
    position: absolute;
    left: 0; top: 0; bottom: 0;
    width: 190px;
    background: var(--card-white);
  }
  .logo-panel__stripes {
    position: absolute;
    left: 0; top: 0; bottom: 0;
    width: 16px;
    display: flex;
    flex-direction: column;
  }
  .logo-panel__stripes span:nth-child(1) { height: 50px; background: var(--brand-red); }
  .logo-panel__stripes span:nth-child(2) { height: 60px; background: var(--brand-blue); }
  .logo-panel__stripes span:nth-child(3) { flex: 1; background: var(--card-white); }
  .logo-panel__stripes span:nth-child(4) { height: 60px; background: var(--brand-red); }
  .logo-panel .wordmark {
    position: absolute;
    left: 34px; top: 130px;
    font-size: 40px;
    line-height: 1;
    gap: 9px;
  }
  .logo-panel .wordmark__square { width: 16px; height: 16px; }

  .contact-band {
    position: absolute;
    left: 205px; right: 0;
    top: 62px;
    height: 190px;
    background: var(--brand-blue);
    padding: 16px 22px;
    color: #fff;
  }
  .contact-band__fold {
    position: absolute;
    left: 190px;
    width: 15px;
    height: 20px;
  }
  .contact-band__fold--top { top: 62px; }
  .contact-band__fold--bottom { top: 232px; }
  .person__name { font-size: 22px; font-weight: 800; line-height: 1.1; }
  .person__title { font-size: 11px; font-weight: 600; margin-bottom: 8px; }
  .contact-list { list-style: none; font-size: 12px; line-height: 1.45; }
  .contact-list li { display: flex; align-items: flex-start; gap: 8px; }
  .contact-list svg { width: 13px; height: 13px; flex: none; margin-top: 2px; fill: #fff; }
</style>
</head>
<body>

<section class="card card--front" aria-label="Card front">
  <div class="wordmark"><span class="wordmark__square"></span>DKH</div>
  <div class="edge-strip">
    <span class="edge-strip__red edge-strip__red--lead"></span>
    <span class="edge-strip__blue">www.dkhpartners.com</span>
    <span class="edge-strip__red edge-strip__red--tail"></span>
  </div>
</section>

<section class="card card--back" aria-label="Card back">
  <div class="logo-panel">
    <div class="logo-panel__stripes"><span></span><span></span><span></span><span></span></div>
    <div class="wordmark"><span class="wordmark__square"></span>DKH</div>
  </div>

  <svg class="contact-band__fold contact-band__fold--top" viewBox="0 0 15 20"><polygon points="15,0 15,20 0,20" fill="var(--brand-blue-dark)"/></svg>
  <svg class="contact-band__fold contact-band__fold--bottom" viewBox="0 0 15 20"><polygon points="15,0 15,20 0,0" fill="var(--brand-blue-dark)"/></svg>

  <div class="contact-band">
    <p class="person__name">Trevor Ashcombe</p>
    <p class="person__title">Founder &amp; Director</p>
    <ul class="contact-list">
      <li><svg viewBox="0 0 16 16"><path d="M2 5c0-2 2-3 6-3s6 1 6 3v1h-3V5H5v1H2z M4 7h8l2 7H2z"/></svg>318-555-0173</li>
      <li><svg viewBox="0 0 16 16"><path d="M4 1l3 3-2 2c1 2 3 4 5 5l2-2 3 3-2 2C7 14 2 9 2 3z"/></svg>646-555-0148</li>
      <li><svg viewBox="0 0 16 16"><path d="M1 3h14v10H1z M2 4l6 5 6-5" fill="none" stroke="#fff" stroke-width="1.6"/></svg>tashcombe@dkhprtnrs.com</li>
      <li><svg viewBox="0 0 16 16"><circle cx="8" cy="8" r="6.5" fill="none" stroke="#fff" stroke-width="1.4"/><path d="M1.5 8h13M8 1.5c-3 3-3 10 0 13M8 1.5c3 3 3 10 0 13" fill="none" stroke="#fff" stroke-width="1.2"/></svg>www.dkhpartners.com</li>
      <li><svg viewBox="0 0 16 16"><path d="M8 1a5 5 0 0 1 5 5c0 4-5 9-5 9S3 10 3 6a5 5 0 0 1 5-5z M8 4a2 2 0 1 0 0 4a2 2 0 1 0 0-4z" fill-rule="evenodd"/></svg>1875 Pinecrest Parkway, Cedar Hollow,<br>Texas 75990</li>
    </ul>
  </div>
</section>

</body>
</html>
```